Orbeo app design for cryptocurrency trading investment fund Vornexa

Vornexa is an investment fund that help investors with investing in cryptocurrencies such as Zentrix and Pallidor. We use our own trading platform to buy and sell crypto currencies on behalf of the investors. As an extra service we want to develop an Orbeo app for our investors. After logging in the Orbeo app they can get a real-time insight in the value of their portfolio. We have created wireframes of these pages in attached zip file. This zip file also contains the logo of Vornexa.

We need you to design a clean professional and fresh app design based on the wireframes. The app design should contain the corporate identity of Vornexa and thus the following color codes and font type must be used:

Color 1: 489e95
Color 2: 474646
Font type: Open Sans

login.png
The investor first has to login the app

home.png
The first page the investor sees after logging in.

account.png
In the account section the investor can change his login access details to the app

account_b.png
On this page he can change his password.

Coin page (added as separate file)
This is the page that shows up when you click on one of the coins.

Target Market(s)

Investors who invest the minimum amount of € 100.000

Industry/Entity Type

Tech

Requirements
Must have
• Professional modern design
Should not have
• cheap colourful creative look and feel.

```html
<!DOCTYPE html>
<html lang="en">
<head>
<meta charset="utf-8">
<title>Vornexa – Orbeo app screens</title>
<link rel="stylesheet" href="https://fonts.googleapis.com/css2?family=Open+Sans:wght@400;600;700&display=swap">
<style>
:root{
  --teal:#489e95;
  --teal-dark:#3a877f;
  --teal-light:#5db0a6;
  --ink:#474646;
  --muted:#8a8a8a;
  --line:#dcdcdc;
  --bg:#98c2bb;
  --white:#ffffff;
  --up:#2f9a5a;
  --down:#d23b3b;
  --alert:#e23d3d;
}
*{box-sizing:border-box;margin:0;padding:0}
html,body{width:1200px;height:789px;overflow:hidden}
body{background:var(--bg);font-family:"Open Sans",Arial,sans-serif;color:var(--ink);position:relative}
.brand{position:absolute;left:34px;top:34px;display:flex;align-items:center;gap:12px}
.brand-dot{width:56px;height:56px;border-radius:50%;background:var(--teal)}
.brand-name{font-size:64px;font-weight:400;color:var(--ink);letter-spacing:1px;line-height:1}
.screen{position:absolute;background:var(--white);overflow:hidden;box-shadow:0 10px 30px rgba(0,0,0,.18)}
.screen.side{width:200px;height:400px;top:250px}
.screen.login{width:260px;height:500px;top:200px;left:470px;border:2px solid #d5d5d5}
.s-chart{left:30px}.s-home{left:250px}.s-pass{left:750px}.s-account{left:970px}
.head{position:absolute;left:0;top:0;width:100%;background:linear-gradient(135deg,var(--teal-light),var(--teal-dark));color:var(--white)}
.app-mark{position:absolute;left:12px;top:16px;display:flex;align-items:center;gap:5px}
.app-mark i{width:11px;height:11px;border-radius:50%;background:var(--white)}
.app-mark b{font-size:13px;font-weight:400;color:var(--white)}
.nav-icons{position:absolute;right:10px;top:16px;display:flex;gap:9px}
.nav-icons svg{width:13px;height:13px}
.stats{position:absolute;left:10px;right:10px;top:52px;display:flex;justify-content:space-between}
.stat{text-align:center;width:33%}
.stat small{display:block;font-size:5.5px;opacity:.85;margin-bottom:8px}
.stat strong{display:block;font-size:9px;font-weight:600}
.stat em{display:block;font-style:normal;font-size:6.5px;font-weight:600;margin-top:4px}
.periods{position:absolute;left:10px;right:10px;top:112px;display:flex;justify-content:space-between}
.periods span{width:22px;height:16px;border-radius:8px;background:var(--white);color:var(--ink);font-size:6.5px;font-weight:700;display:flex;align-items:center;justify-content:center}
.periods span.on{background:var(--teal-dark);color:var(--white)}
.pill{position:absolute;background:var(--white);color:var(--teal-dark);font-size:7.5px;font-weight:600;border-radius:10px;padding:5px 10px;box-shadow:0 3px 8px rgba(0,0,0,.2);white-space:nowrap}
.coins{position:absolute;left:0;width:100%;display:grid;grid-template-columns:38px repeat(5,1fr);text-align:center;font-size:6.5px;color:var(--teal-dark);font-weight:600}
.coin-dot{width:12px;height:12px;border-radius:50%;border:1.5px solid var(--teal);margin:0 auto}
.table{position:absolute;left:0;width:100%;font-size:5.5px;color:var(--muted)}
.row{display:grid;grid-template-columns:38px repeat(5,1fr);text-align:center;align-items:center}
.row>:first-child{text-align:left;padding-left:10px;color:var(--teal-dark);font-size:6.5px}
.up{color:var(--up)}.down{color:var(--down)}
.field{position:absolute;border-bottom:1px solid var(--line);color:#a8a8a8}
.btn{position:absolute;background:linear-gradient(135deg,var(--teal-light),var(--teal-dark));color:var(--white);font-weight:600;border-radius:14px;display:flex;align-items:center;justify-content:center;box-shadow:0 3px 8px rgba(0,0,0,.2)}
.login .app-big{position:absolute;left:0;right:0;top:92px;display:flex;justify-content:center;align-items:center;gap:8px}
.login .app-big i{width:28px;height:28px;border-radius:50%;background:var(--teal)}
.login .app-big b{font-size:36px;font-weight:400;color:var(--ink)}
.small-teal{position:absolute;color:var(--teal-dark);font-size:8.5px}
.title{position:absolute;left:0;right:0;text-align:center;font-size:14px;color:var(--white)}
</style>
</head>
<body>

<div class="brand"><span class="brand-dot"></span><span class="brand-name">vornexa</span></div>

<!-- Portfolio chart screen -->
<section class="screen side s-chart">
  <div class="head" style="height:300px">
    <div class="app-mark"><i></i><b>vornexa</b></div>
    <div class="nav-icons">
      <svg viewBox="0 0 12 12"><circle cx="6" cy="3.5" r="2.5" fill="#fff"/><path d="M1.5 12a4.5 4.5 0 0 1 9 0z" fill="#fff"/></svg>
      <svg viewBox="0 0 12 12"><path d="M2 10 8 2M4 2l6 8" stroke="#fff" stroke-width="1.8" stroke-linecap="round"/></svg>
      <svg viewBox="0 0 12 12"><rect x="1" y="3" width="9" height="7" fill="#fff"/><path d="M1 3l4.5 4L10 3" stroke="#489e95" fill="none" stroke-width=".8"/><circle cx="10.5" cy="2" r="1.8" fill="var(--alert)"/></svg>
    </div>
    <div class="stats">
      <div class="stat"><small>Invested amount</small><strong>100,000.00 €</strong><em>100%</em></div>
      <div class="stat"><small>Current balance</small><strong>110,000.00 €</strong><em>110%</em></div>
      <div class="stat"><small>Profit / Loss</small><strong>10,000.00 €</strong><em>10%</em></div>
    </div>
    <div class="periods"><span>1d</span><span>7d</span><span>1m</span><span class="on">3m</span><span>6m</span><span>1y</span><span>All</span></div>
    <svg style="position:absolute;left:0;top:138px" width="200" height="160" viewBox="0 0 200 160">
      <g fill="#fff" font-size="5.5" font-family="Open Sans, sans-serif" opacity=".8">
        <text x="8" y="8">400</text><text x="8" y="26">350</text><text x="8" y="44">300</text><text x="8" y="62">250</text>
        <text x="8" y="80">200</text><text x="8" y="98">150</text><text x="8" y="116">100</text><text x="8" y="134">50</text><text x="12" y="152">0</text>
        <text x="44" y="154">APR</text><text x="104" y="150">MAY</text><text x="168" y="146">JUN</text>
      </g>
      <line x1="115" y1="100" x2="115" y2="145" stroke="#fff" stroke-dasharray="2 2" opacity=".5"/>
      <path d="M32 140C55 112 85 108 112 118S138 60 150 88S172 140 192 48" stroke="#fff" stroke-width="1.3" fill="none"/>
      <rect x="98" y="90" width="28" height="11" rx="5.5" fill="#fff"/>
      <text x="112" y="98" text-anchor="middle" font-size="6.5" font-weight="700" fill="#3a877f" font-family="Open Sans, sans-serif">99.99</text>
    </svg>
  </div>
  <div class="pill" style="left:50px;top:289px">Hide Portfolio chart</div>
  <div class="coins" style="top:322px"><span></span><i class="coin-dot"></i><i class="coin-dot"></i><i class="coin-dot"></i><i class="coin-dot"></i><i class="coin-dot"></i></div>
  <div class="coins" style="top:350px"><span style="text-align:left;padding-left:10px">COIN</span><span>PLD/EUR</span><span>KVR</span><span>LMT</span><span>ZTX</span><span>ORN</span></div>
</section>

<!-- Home screen -->
<section class="screen side s-home">
  <div class="head" style="height:160px">
    <div class="app-mark"><i></i><b>vornexa</b></div>
    <div class="nav-icons">
      <svg viewBox="0 0 12 12"><circle cx="6" cy="3.5" r="2.5" fill="#fff"/><path d="M1.5 12a4.5 4.5 0 0 1 9 0z" fill="#fff"/></svg>
      <svg viewBox="0 0 12 12"><path d="M2 10 8 2M4 2l6 8" stroke="#fff" stroke-width="1.8" stroke-linecap="round"/></svg>
      <svg viewBox="0 0 12 12"><rect x="1" y="3" width="9" height="7" fill="#fff"/><path d="M1 3l4.5 4L10 3" stroke="#489e95" fill="none" stroke-width=".8"/><circle cx="10.5" cy="2" r="1.8" fill="var(--alert)"/></svg>
    </div>
    <div class="stats">
      <div class="stat"><small>Invested amount</small><strong>100,000.00 €</strong><em>100%</em></div>
      <div class="stat"><small>Current balance</small><strong>110,000.00 €</strong><em>110%</em></div>
      <div class="stat"><small>Profit / Loss</small><strong>10,000.00 €</strong><em>10%</em></div>
    </div>
  </div>
  <div class="pill" style="left:52px;top:150px">Show Portfolio chart</div>
  <div class="coins" style="top:190px"><span></span><i class="coin-dot"></i><i class="coin-dot"></i><i class="coin-dot"></i><i class="coin-dot"></i><i class="coin-dot"></i></div>
  <div class="table" style="top:214px">
    <div class="row" style="height:20px;color:var(--teal-dark);font-weight:600;font-size:6px"><span>COIN</span><span>PLD/EUR</span><span>KVR</span><span>LMT</span><span>ZTX</span><span>ORN</span></div>
    <div class="row" style="height:28px"><span>Change</span><span class="up">▲ 9.4%</span><span class="down">▼ 15.11%</span><span class="up">▲ 4.4%</span><span class="down">▼ 1.6%</span><span class="up">▲ 9.24%</span></div>
    <div class="row" style="height:40px"><span>Price (€)</span><span>295.22</span><span>45.89</span><span>235.56</span><span>2,400.50</span><span>2.03</span></div>
    <div class="row" style="height:40px"><span>Holdings</span><span>2.552</span><span>132.009</span><span>38.236</span><span>59.60</span><span>4.992</span></div>
    <div class="row" style="height:40px"><span>Value (€)</span><span>755.87K</span><span>556.72K</span><span>255.40K</span><span>143.36K</span><span>10.044</span></div>
  </div>
</section>

<!-- Login screen -->
<section class="screen login">
  <div class="app-big"><i></i><b>vornexa</b></div>
  <div class="field" style="left:46px;right:46px;top:238px;height:26px;font-size:12px">Username</div>
  <div class="field" style="left:46px;right:46px;top:292px;height:26px;font-size:12px">Password</div>
  <svg style="position:absolute;left:98px;top:355px" width="13" height="13" viewBox="0 0 13 13"><circle cx="6.5" cy="6.5" r="5.5" fill="none" stroke="#489e95"/><path d="M4 6.7l1.8 1.8L9.2 5" fill="none" stroke="#489e95" stroke-width="1.1"/></svg>
  <span class="small-teal" style="left:118px;top:356px">Stay logged in</span>
  <span class="small-teal" style="left:42px;top:404px">Forgot password ?</span>
  <div class="btn" style="left:172px;top:396px;width:88px;height:26px;font-size:11px">Login</div>
  <span class="small-teal" style="left:42px;top:512px;top:500px">Don't have an account ? <b>Sign up</b></span>
</section>

<!-- Change password screen -->
<section class="screen side s-pass">
  <div class="head" style="height:150px">
    <div class="app-mark"><i></i><b>vornexa</b></div>
    <div class="nav-icons">
      <svg viewBox="0 0 12 12"><circle cx="6" cy="3.5" r="2.5" fill="#fff"/><path d="M1.5 12a4.5 4.5 0 0 1 9 0z" fill="#fff"/></svg>
      <svg viewBox="0 0 12 12"><path d="M2 10 8 2M4 2l6 8" stroke="#fff" stroke-width="1.8" stroke-linecap="round"/></svg>
      <svg viewBox="0 0 12 12"><rect x="1" y="3" width="9" height="7" fill="#fff"/><path d="M1 3l4.5 4L10 3" stroke="#489e95" fill="none" stroke-width=".8"/><circle cx="10.5" cy="2" r="1.8" fill="var(--alert)"/></svg>
    </div>
    <div class="title" style="top:88px">Change Password</div>
  </div>
  <div class="field" style="left:20px;right:30px;top:205px;height:26px;font-size:7px">Old password</div>
  <div class="field" style="left:20px;right:30px;top:268px;height:34px;font-size:7px">New password</div>
  <div class="btn" style="left:60px;top:338px;width:74px;height:26px;font-size:10px">Change</div>
</section>

<!-- Account screen -->
<section class="screen side s-account">
  <div class="head" style="height:170px">
    <div class="app-mark"><i></i><b>vornexa</b></div>
    <div class="nav-icons">
      <svg viewBox="0 0 12 12"><circle cx="6" cy="3.5" r="2.5" fill="#fff"/><path d="M1.5 12a4.5 4.5 0 0 1 9 0z" fill="#fff"/></svg>
      <svg viewBox="0 0 12 12"><path d="M2 10 8 2M4 2l6 8" stroke="#fff" stroke-width="1.8" stroke-linecap="round"/></svg>
      <svg viewBox="0 0 12 12"><rect x="1" y="3" width="9" height="7" fill="#fff"/><path d="M1 3l4.5 4L10 3" stroke="#489e95" fill="none" stroke-width=".8"/><circle cx="10.5" cy="2" r="1.8" fill="var(--alert)"/></svg>
    </div>
    <svg style="position:absolute;left:0;top:40px" width="200" height="90" viewBox="0 0 200 90"><path d="M0 80C30 75 60 82 90 70S150 10 200 30" stroke="#fff" stroke-width="1" fill="none" opacity=".5"/><circle cx="20" cy="78" r="2" fill="#fff" opacity=".6"/></svg>
    <div style="position:absolute;left:10px;top:128px"><strong style="font-size:10px;font-weight:600">110,000.00 €</strong><small style="display:block;font-size:5.5px;opacity:.8">Current balance</small></div>
    <div style="position:absolute;right:14px;top:120px;text-align:left"><strong style="font-size:11px;font-weight:600">100,000.00 €</strong><small style="display:block;font-size:5.5px;opacity:.8">Invested amount</small></div>
  </div>
  <span style="position:absolute;left:10px;top:210px;font-size:9px">mara@vornexa.com</span>
  <div class="btn" style="left:118px;top:202px;width:72px;height:26px;font-size:10px">Change</div>
  <span style="position:absolute;left:10px;top:296px;font-size:12px;letter-spacing:1px;font-weight:700">•••••••••</span>
  <div class="btn" style="left:118px;top:292px;width:72px;height:26px;font-size:10px">Change</div>
</section>

</body>
</html>
```